Torvane Facilities Business Card Design

We would now like to design business cards with the new Torvane Facilities logo

Target Market(s)

Professional

Industry/Entity Type

Professional services

Contact Information for Business Card

Employee name, title, phone number, email address, corporate office address and logo.

Font styles to use
Sans Serif

Colors
0054AA
0677BA
7BADD7
CADEEF
E8F1F8

Requirements
Must have
• My logo
Should not have
• any other pictures or images besides my logo

```html
<!DOCTYPE html>
<html lang="en">
<head>
<meta charset="utf-8">
<title>Torvane Facilities Business Card</title>
<link href="https://fonts.googleapis.com/css2?family=Open+Sans:wght@400;700&display=swap" rel="stylesheet">
<style>
  :root {
    --bg: #3a3a3a;
    --card: #1b1b1b;
    --blue: #3a7fcf;
    --text: #e6e6e6;
    --gloss: #6a6a6a;
  }
  * { margin: 0; padding: 0; box-sizing: border-box; }
  html, body { width: 1200px; height: 801px; overflow: hidden; }
  body {
    background: var(--bg);
    font-family: "Open Sans", Arial, sans-serif;
    position: relative;
  }
  .card {
    position: absolute;
    width: 530px;
    height: 303px;
    background: var(--card);
    border-bottom: 3px solid var(--blue);
  }
  .card-front { left: 45px; top: 120px; }
  .card-back { left: 625px; top: 378px; }

  .front-brand {
    position: absolute;
    left: 40px; top: 0; bottom: 0;
    width: 230px;
    display: flex; align-items: center; gap: 12px;
  }
  .brand-square {
    width: 22px; height: 22px;
    background: var(--blue);
    flex: none;
  }
  .brand-name {
    font-size: 24px; font-weight: 700;
    color: var(--blue);
    line-height: 1.15;
  }
  .divider {
    position: absolute;
    left: 285px; top: 70px;
    width: 1.5px; height: 165px;
    background: var(--blue);
  }
  .contact {
    position: absolute;
    left: 305px; top: 72px;
    color: var(--text);
    font-size: 13px;
    line-height: 1.45;
  }
  .person-name {
    color: var(--blue);
    font-weight: 700;
    font-size: 17px;
    letter-spacing: 0.5px;
  }
  .person-title { margin-bottom: 10px; }
  .address { margin-bottom: 10px; }
  .contact-line { display: flex; align-items: center; gap: 7px; }
  .contact-line svg { width: 11px; height: 11px; flex: none; }

  .back-brand {
    position: absolute;
    inset: 0;
    display: flex; align-items: center; justify-content: center; gap: 16px;
  }
  .back-brand .brand-square { background: var(--gloss); width: 34px; height: 34px; }
  .back-brand .brand-name { color: var(--gloss); font-size: 38px; }
</style>
</head>
<body>
  <section class="card card-front">
    <div class="front-brand">
      <span class="brand-square"></span>
      <span class="brand-name">Torvane<br>Facilities</span>
    </div>
    <div class="divider"></div>
    <div class="contact">
      <div class="person-name">DANA KELLERBY</div>
      <div class="person-title">CEO</div>
      <div class="address">1480 Harbor Mill Road<br>Easton Falls, MA 017</div>
      <div class="contact-line">
        <svg viewBox="0 0 12 12"><circle cx="6" cy="6" r="6" fill="var(--blue)"/><path d="M4 3.2l1 1.6-.6.7c.4.9 1.1 1.6 2 2l.7-.6 1.6 1-.5 1c-2.4-.3-4.4-2.3-4.7-4.7z" fill="#1b1b1b"/></svg>
        555-218-6402
      </div>
      <div class="contact-line">
        <svg viewBox="0 0 12 12"><rect x="1" y="2.5" width="10" height="7" fill="var(--blue)"/><path d="M1 2.5l5 4 5-4" stroke="#1b1b1b" stroke-width="1" fill="none"/></svg>
        dkellerby@torvane.com
      </div>
      <div class="contact-line">
        <svg viewBox="0 0 12 12"><circle cx="6" cy="6" r="5.5" fill="var(--blue)"/><path d="M.5 6h11M6 .5c-2.5 3-2.5 8 0 11M6 .5c2.5 3 2.5 8 0 11" stroke="#1b1b1b" stroke-width=".8" fill="none"/></svg>
        www.torvane.com
      </div>
    </div>
  </section>

  <section class="card card-back">
    <div class="back-brand">
      <span class="brand-square"></span>
      <span class="brand-name">Torvane Facilities</span>
    </div>
  </section>
</body>
</html>
```